Label Design for honey from a small farm in Italy

We need a label for our Acacia's honey .
We are a little farm in Italy and we would like something like organic, raw and simple.
Maybe with botanical drawing with different color like watercolor o something like that (very important natural and easy)
the jar for 1kg of honey: Capacity: 780 ml - Height: 137 mm - Diameter: ∅ 94 mm
- size approx h 5,5 x 10/14cm ( we use the same label for kg and 500 gr jar)

Industry/Entity Type

Farm

Requirements
Must have
• the writings:
- Acacia
- Miele italiano di Acacia
- Da consumarsi preferibilmente entro: ( and below the space to put the date by the hands)
- some space to put some presentation of the farm or some phrases
- our logo
- the space to put the weight by the hands
- Prodotto da Azienda Agricola ...(produced by Farm Name and address....)
- Confezionato presso Apicoltura... (packaged at apiculture Name and address..)
- graphic of Acacia’s flowers ( like drawing)
Should not have
• Barcode
nutritional table

```html
<!DOCTYPE html>
<html lang="it">
<head>
<meta charset="utf-8">
<title>Miele Italiano – Acacia</title>
<link href="https://fonts.googleapis.com/css2?family=Josefin+Sans:wght@600;700&family=Oswald:wght@500&family=EB+Garamond:ital@1&family=Courier+Prime:wght@400;700&family=Montserrat:wght@400;500&family=Homemade+Apple&display=swap" rel="stylesheet">
<style>
  :root {
    --paper: #d4e0bd;
    --ink: #363c0c;
    --leaf: #2f8a1e;
    --sage: #b9c9a0;
  }
  * { margin: 0; padding: 0; box-sizing: border-box; }
  html, body { width: 1200px; height: 490px; overflow: hidden; background: var(--paper); }
  .label { position: relative; width: 1200px; height: 490px; background: var(--paper); color: var(--ink); }
  .abs { position: absolute; white-space: nowrap; }

  .headline { left: 0; width: 1196px; top: 28px; text-align: center; font: 700 21px "Josefin Sans", sans-serif; letter-spacing: 6px; }

  .botanical { left: 510px; top: 66px; width: 196px; height: 254px; }

  .recipes { left: 192px; top: 105px; }
  .recipes-title { font: 500 13px "Oswald", sans-serif; letter-spacing: 0.2px; }
  .recipes-sub { font: italic 15px "EB Garamond", serif; letter-spacing: -0.4px; margin-top: 4px; }
  .recipes-list { list-style: none; font: italic 11px "EB Garamond", serif; letter-spacing: -0.3px; line-height: 19.4px; margin-top: 1px; }

  .variety { left: 504px; top: 270px; font: 700 43px "Josefin Sans", sans-serif; color: var(--leaf); letter-spacing: 9px; }
  .latin { left: 714px; top: 282px; font: 700 9px "Courier Prime", monospace; line-height: 14px; letter-spacing: 0.6px; }

  .info-box { left: 187px; top: 321px; width: 826px; height: 142px; border: 5px solid var(--ink); }
  .rule-v, .rule-h { position: absolute; background: var(--ink); }
  .rule-v { top: 0; bottom: 0; width: 3px; }
  .rule-h { height: 2px; }

  .mono { font: 700 9.5px "Courier Prime", monospace; letter-spacing: 0.8px; }
  .mono-green { font: 700 9.5px "Courier Prime", monospace; letter-spacing: 0.8px; color: var(--leaf); }
  .pi-label { font: 700 13px "Courier Prime", monospace; letter-spacing: 1px; }
  .pi-number { font: 400 15px "Courier Prime", monospace; letter-spacing: 1.5px; color: var(--leaf); }
  .signature { font: 400 11px "Homemade Apple", cursive; color: var(--leaf); }
  .weight-label { font: 700 12px "Courier Prime", monospace; letter-spacing: 1.5px; }

  .brand { display: flex; align-items: center; gap: 6px; font: 500 13px "Oswald", sans-serif; letter-spacing: 0.5px; }
  .brand-square { width: 9px; height: 9px; background: var(--ink); }

  .vertical { writing-mode: vertical-rl; transform: rotate(180deg); }
  .contact { font: 400 8.5px "Montserrat", sans-serif; }
  .side-sub { font: 500 11px "Montserrat", sans-serif; }
  .side-name { font: 500 20px "Montserrat", sans-serif; }
</style>
</head>
<body>
<main class="label">
  <h1 class="abs headline">MIELE ITALIANO</h1>

  <svg class="abs botanical" role="img" aria-label="Illustrazione botanica di un ramo di acacia con foglie verdi e grappoli di fiori bianchi" viewBox="0 0 196 254" preserveAspectRatio="none">
    <defs>
      <radialGradient id="bloom" cx="50%" cy="45%" r="55%">
        <stop offset="0" stop-color="#4f7a3a" stop-opacity="0.55"/>
        <stop offset="0.6" stop-color="#8aa777" stop-opacity="0.35"/>
        <stop offset="1" stop-color="#d4e0bd" stop-opacity="0"/>
      </radialGradient>
    </defs>
    <rect width="196" height="254" fill="url(#bloom)"/>
  </svg>

  <section class="abs recipes">
    <h2 class="recipes-title">RAFFINATEZZE CULINARIE</h2>
    <p class="recipes-sub">con il miele di Acacia</p>
    <ul class="recipes-list">
      <li>- Mantecare un risotto alla camomilla</li>
      <li>- Addolcire il caffè e lo yogurt naturale</li>
      <li>- Accompagnare un formaggio</li>
      <li>&nbsp;fresco di capra</li>
      <li>- Emulsionare nel condimento</li>
      <li>&nbsp;dell' insalata o del roast-beef</li>
    </ul>
  </section>

  <p class="abs variety">ACACIA</p>
  <p class="abs latin">Nome scientifico:<br>Robinia Pseudoacacia</p>

  <section class="abs info-box">
    <span class="rule-v" style="left:161px"></span>
    <span class="rule-v" style="left:652px"></span>
    <span class="rule-h" style="left:163px; right:0; top:43px"></span>
    <span class="rule-h" style="left:163px; right:0; top:82px"></span>

    <div class="abs brand" style="left:42px; top:59px">
      <span class="brand-square"></span>IL POGGIO
    </div>

    <p class="abs mono" style="left:180px; top:15px">Smielato e confezionato presso</p>
    <p class="abs mono-green" style="left:422px; top:13px">Apicoltura Bernasconi Elio</p>
    <p class="abs mono-green" style="left:422px; top:31px">Via dei Tigli 12, 21100 Borgoverde</p>

    <p class="abs mono" style="left:183px; top:53px">Prodotto da Azienda Agricola Il Poggio</p>
    <p class="abs mono" style="left:241px; top:72px">Società Semplice di</p>
    <p class="abs signature" style="left:403px; top:64px">Rinaldi M. <span style="font-family:'Courier Prime',monospace;font-weight:700;font-size:9.5px;color:var(--ink)">e</span> Galli T.</p>

    <p class="abs mono" style="left:179px; top:111px">Da consumarsi preferibilmente entro il</p>

    <p class="abs pi-label" style="left:662px; top:10px">PI:</p>
    <p class="abs pi-number" style="left:683px; top:28px">01928374650</p>
    <p class="abs mono" style="left:661px; top:56px">Via Roma 5, 21010,</p>
    <p class="abs mono" style="left:668px; top:70px">Castelnuovo (Va)</p>
    <p class="abs weight-label" style="left:659px; top:110px">Peso</p>
  </section>

  <p class="abs vertical contact" style="left:1108px; bottom:188px">ig @ilpoggiorinaldi&nbsp;&nbsp;fb @ilpoggiorinaldi</p>
  <p class="abs vertical contact" style="left:1129px; bottom:188px">e-mail&nbsp;&nbsp;ilpoggiorinaldi@example.com</p>
  <p class="abs vertical contact" style="left:1150px; bottom:188px">tel. +39 000 11 22 333</p>

  <div class="abs vertical brand" style="left:1092px; bottom:34px">
    <span class="brand-square"></span>IL POGGIO
  </div>
  <p class="abs vertical side-sub" style="left:1126px; bottom:34px">Azienda Agricola</p>
  <p class="abs vertical side-name" style="left:1145px; bottom:34px">Il Poggio</p>
</main>
</body>
</html>
```